Ferris + Oakdale Architecture Ltd Stationary rebrand Lead designer to create a fresh clean modern...

We have recieved a great new logo design and now we are after a consistant fresh and modern stationary to match the new design. Business card design, Letter Head design, presentatnion folders and other stationery within the package. I have also added some of our existing layouts for presentation we would like updating with the new look, We would like a clean modern fresh design that looks visually pleasing on the page. we cant wait to see what you come up with!!!!

Target Market(s)

young professionals and middle age clients

Industry/Entity Type

Architect

Contact Information for Business Card

i have uploarded our orginal business card that has all the details attached.

Font styles to use
Sans Serif

Colors
000000
ffffff
d3d3d3

Requirements
Must have
• Logo and our contact information
Nice to have
• white sape around the card to give a clean look.

```html
<!DOCTYPE html>
<html lang="en">
<head>
<meta charset="utf-8">
<title>Ferris + Oakdale Architecture – Presentation Sheets</title>
<link rel="stylesheet" href="https://fonts.googleapis.com/css2?family=Montserrat:wght@500;600;700&display=swap">
<style>
  :root {
    --backdrop: #87888a;
    --paper: #ffffff;
    --ink: #000000;
    --mist: #d3d3d3;
    --muted: #6d6d6d;
    --caption: #4a4a4a;
    --accent: #e0502a;
    --placeholder: #cdd1d6;
  }
  * { margin: 0; padding: 0; box-sizing: border-box; }
  html, body { width: 1200px; height: 1200px; overflow: hidden; }
  body {
    background: var(--backdrop);
    font-family: "Montserrat", sans-serif;
    color: var(--ink);
    position: relative;
  }
  .sheet {
    position: absolute;
    background: var(--paper);
    overflow: hidden;
  }
  .sheet--landscape { left: 32px; top: 28px; width: 730px; height: 564px; }
  .sheet--portrait { left: 738px; top: 611px; width: 419px; height: 544px; }

  .corner-frame {
    position: absolute;
    border-style: solid;
    border-color: var(--mist);
    transform: rotate(-30deg);
  }
  .sheet--landscape .corner-frame { left: 508px; top: 40px; width: 210px; height: 210px; border-width: 24px; }
  .sheet--portrait .corner-frame { left: 335px; top: 13px; width: 76px; height: 76px; border-width: 9px; }

  .brand {
    position: absolute;
    display: flex;
    align-items: center;
    gap: 7px;
  }
  .brand__square { border: 6px solid var(--ink); }
  .brand__name {
    font-weight: 600;
    text-transform: uppercase;
    line-height: 1.2;
    white-space: nowrap;
  }
  .brand__line1 { display: block; letter-spacing: 0.09em; }
  .brand__line2 { display: block; font-weight: 500; letter-spacing: 0.62em; }

  .sheet--landscape .brand { left: 21px; top: 18px; }
  .sheet--landscape .brand__square { width: 48px; height: 48px; }
  .sheet--landscape .brand__line1 { font-size: 14.5px; }
  .sheet--landscape .brand__line2 { font-size: 9px; }

  .sheet--portrait .brand { left: 14px; top: 14px; gap: 5px; }
  .sheet--portrait .brand__square { width: 37px; height: 37px; border-width: 5px; }
  .sheet--portrait .brand__line1 { font-size: 10.5px; }
  .sheet--portrait .brand__line2 { font-size: 6.6px; }

  .drawing-key {
    position: absolute;
    left: 74px;
    top: 156px;
    list-style: none;
    font-size: 5.6px;
    font-weight: 700;
    letter-spacing: 0.14em;
    color: var(--muted);
  }
  .drawing-key__title {
    font-size: 6.4px;
    letter-spacing: 0.2em;
    margin-bottom: 1px;
  }
  .drawing-key li { height: 10.3px; display: flex; gap: 12px; white-space: nowrap; }
  .drawing-key .num { width: 8px; }
  .drawing-key .is-final { color: var(--accent); }

  .render {
    position: absolute;
    background: var(--placeholder);
  }
  .render--street-a { left: 202px; top: 163px; width: 244px; height: 158px; }
  .render--street-b { left: 202px; top: 340px; width: 244px; height: 143px; }
  .render--house-a { left: 75px; top: 109px; width: 276px; height: 161px; }
  .render--house-b { left: 75px; top: 286px; width: 276px; height: 164px; }

  .caption {
    position: absolute;
    left: 0; right: 0;
    top: 466px;
    text-align: center;
    color: var(--caption);
  }
  .caption__title { font-size: 6.2px; font-weight: 700; letter-spacing: 0.45em; }
  .caption__sub { font-size: 5.4px; font-weight: 600; letter-spacing: 0.45em; margin-top: 4px; }
  .caption__note { font-size: 3.2px; font-weight: 500; margin-top: 4px; }
</style>
</head>
<body>

<section class="sheet sheet--landscape">
  <span class="corner-frame"></span>
  <div class="brand">
    <span class="brand__square"></span>
    <span class="brand__name"><span class="brand__line1">Ferris + Oakdale</span><span class="brand__line2">Architecture</span></span>
  </div>

  <ul class="drawing-key">
    <li class="drawing-key__title">KEY TO DRAWINGS</li>
    <li><span class="num">01</span>LOCATION PLAN</li>
    <li><span class="num">02</span>PROPOSED SITE PLAN</li>
    <li><span class="num">03</span>GROUND FLOOR PLAN</li>
    <li><span class="num">04</span>FIRST FLOOR PLAN</li>
    <li><span class="num">05</span>ELEVATIONS</li>
    <li><span class="num">06</span>ELEVATIONS</li>
    <li><span class="num">07</span>ROOF PLAN</li>
    <li><span class="num">08</span>SECTIONS A-A</li>
    <li><span class="num">09</span>SECTIONS B-B</li>
    <li><span class="num">10</span>DOOR SCHEDULE</li>
    <li><span class="num">11</span>WINDOW SCHEDULE</li>
    <li><span class="num">12</span>WINDOW SCHEDULE</li>
    <li><span class="num">13</span>DRAINAGE LAYOUT</li>
    <li><span class="num">14</span>FLOOR FINISHES LAYOUT</li>
    <li><span class="num">15</span>WALL BUILD-UPS</li>
    <li><span class="num">16</span>REFLECTED CEILING PLAN</li>
    <li><span class="num">17</span>GLASS DETAILS</li>
    <li><span class="num">18</span>GLASS DETAILS</li>
    <li><span class="num">19</span>GLASS DETAILS</li>
    <li><span class="num">20</span>GLASS DETAILS</li>
    <li><span class="num">21</span>CONSTRUCTION DETAILS</li>
    <li><span class="num">22</span>CONSTRUCTION DETAILS</li>
    <li><span class="num">23</span>CONSTRUCTION DETAILS</li>
    <li><span class="num">24</span>CONSTRUCTION DETAILS</li>
    <li><span class="num">25</span>CONSTRUCTION DETAILS</li>
    <li><span class="num">26</span>CONSTRUCTION DETAILS</li>
    <li><span class="num">27</span>CONSTRUCTION DETAILS</li>
    <li><span class="num">28</span>CONSTRUCTION DETAILS</li>
    <li><span class="num">29</span>CONSTRUCTION DETAILS</li>
    <li><span class="num">30</span>CONSTRUCTION DETAILS</li>
    <li class="is-final"><span class="num">31</span>SPECIFICATION</li>
  </ul>

  <div class="render render--street-a" role="img" aria-label="Street-corner render of a two-storey commercial building"></div>
  <div class="render render--street-b" role="img" aria-label="Side street render of the commercial building"></div>
</section>

<section class="sheet sheet--portrait">
  <span class="corner-frame"></span>
  <div class="brand">
    <span class="brand__square"></span>
    <span class="brand__name"><span class="brand__line1">Ferris + Oakdale</span><span class="brand__line2">Architecture</span></span>
  </div>

  <div class="render render--house-a" role="img" aria-label="Concept render of a modern house seen across a lawn"></div>
  <div class="render render--house-b" role="img" aria-label="Second concept render of the modern house from another angle"></div>

  <div class="caption">
    <p class="caption__title">LINDEN HOUSE CONCEPT</p>
    <p class="caption__sub">PERSPECTIVES</p>
    <p class="caption__note">Concept imagery for client review only, subject to planning approval and detailed design development.</p>
  </div>
</section>

</body>
</html>
```